Need a logo/cover design for my book Golden Handshake Hours: How We Turned Coffee Chats Into Fortunes With Friends Worth Keeping

Over the years I've worked in chambers of commerce and at high-profile country clubs and have had access to very successful people and the companies they work for or launch. Through meeting people, learning from them, applying what I've learned, and by connecting with them as resources and lead sources for business, I've been able to generate over $2M in the past few years. I'm sharing the roadmap I followed to create the connections and make the sales.
Updates

Combination of slow feedback on my part by not understanding the process, similar designs, and many who withdrew immediately after my first response.

Target Market(s)

Entrepreneurs and business people, specifically business owners and those in sales and marketing roles.

Industry/Entity Type

Small Business

Font styles to use
Sans Serif

Colors

Designer to choose colors to be used in the design.

Requirements
Must have
• Original graphic design. Something that looks like I paid a professional to have it done.
Nice to have
• Perhaps my picture? Not really sure
Should not have
• I'd like to avoid a look that I could have created myself using clip art and special fonts.

```html
<!DOCTYPE html>
<html lang="en">
<head>
<meta charset="utf-8">
<title>Golden Handshake Hours — Book Cover</title>
<link rel="stylesheet" href="https://fonts.googleapis.com/css2?family=Bebas+Neue&family=Montserrat:wght@300;400;500&display=swap">
<style>
  :root {
    --page: #ffffff;
    --back-taupe: #a09383;
    --title-red: #8e1f1d;
    --title-gold: #6f5520;
    --ink: #1d1a18;
    --bio-band: #e8dcda;
    --barcode-box: #ffffff;
    --scene-top: #d8cdc4;
    --scene-mid: #e6d6d2;
    --scene-crowd: #b49aa0;
    --scene-crowd-dark: #8c7479;
    --scene-table: #f4f2f1;
  }
  * { box-sizing: border-box; margin: 0; padding: 0; }
  html, body { width: 1200px; height: 1200px; overflow: hidden; background: var(--page); }
  .canvas { position: relative; width: 1200px; height: 1200px; }

  .book-wrap {
    position: absolute; left: 81px; top: 207px; width: 1036px; height: 782px;
    background: var(--back-taupe); overflow: hidden;
  }

  /* Back cover */
  .back-cover { position: absolute; left: 0; top: 0; width: 528px; height: 782px; }
  .blurb {
    position: absolute; left: 49px; top: 56px; width: 406px;
    font-family: "Montserrat", sans-serif; font-weight: 400;
    font-size: 12.4px; line-height: 19.2px; color: var(--ink);
    text-align: justify;
  }
  .blurb p + p { margin-top: 19px; }
  .author-band {
    position: absolute; left: 0; top: 522px; width: 506px; height: 107px;
    background: var(--bio-band);
  }
  .author-photo {
    position: absolute; left: 38px; top: 0; width: 122px; height: 107px;
    background: linear-gradient(135deg, #9a5a48 0%, #7c8a98 55%, #5d6f80 100%);
  }
  .author-bio {
    position: absolute; left: 172px; top: 3px; width: 318px;
    font-family: "Montserrat", sans-serif; font-size: 11.2px; line-height: 16.6px;
    color: var(--ink);
  }
  .barcode-box {
    position: absolute; left: 275px; top: 646px; width: 182px; height: 102px;
    background: var(--barcode-box);
  }

  /* Spine */
  .spine-title {
    position: absolute; left: 424px; top: 378px; width: 194px; height: 24px;
    transform: rotate(90deg); transform-origin: 50% 50%;
    font-family: "Bebas Neue", sans-serif; font-size: 21px; line-height: 24px;
    text-align: center; letter-spacing: 0.3px;
    color: var(--title-red); white-space: nowrap;
  }

  /* Front cover */
  .front-cover { position: absolute; left: 528px; top: 0; width: 508px; height: 782px; }
  .front-scene {
    position: absolute; inset: 0;
    background:
      radial-gradient(ellipse 46% 16% at 74% 88%, var(--scene-table) 0%, rgba(244,242,241,0.85) 55%, rgba(244,242,241,0) 100%),
      radial-gradient(ellipse 30% 14% at 62% 64%, rgba(140,116,121,0.55) 0%, rgba(140,116,121,0) 100%),
      radial-gradient(ellipse 34% 18% at 18% 70%, rgba(140,116,121,0.6) 0%, rgba(140,116,121,0) 100%),
      radial-gradient(ellipse 26% 14% at 90% 66%, rgba(120,96,104,0.55) 0%, rgba(120,96,104,0) 100%),
      radial-gradient(ellipse 22% 16% at 10% 92%, rgba(180,154,160,0.8) 0%, rgba(180,154,160,0) 100%),
      linear-gradient(180deg, var(--scene-top) 0%, #e4dad2 36%, var(--scene-mid) 56%, var(--scene-crowd) 78%, #c3adb0 100%);
  }
  .book-title {
    position: absolute; left: 0; top: 30px; width: 508px;
    font-family: "Bebas Neue", sans-serif; font-weight: 400;
    font-size: 122px; line-height: 114px; text-align: center; letter-spacing: 1px;
  }
  .book-title span { display: block; }
  .title-red { color: var(--title-red); }
  .title-gold { color: var(--title-gold); }
  .book-subtitle {
    position: absolute; left: 40px; top: 396px; width: 430px;
    font-family: "Montserrat", sans-serif; font-weight: 300;
    font-size: 26px; line-height: 34px; text-align: center; color: var(--ink);
  }
  .author-name {
    position: absolute; left: 0; top: 715px; width: 508px;
    font-family: "Montserrat", sans-serif; font-weight: 500;
    font-size: 25px; letter-spacing: 1px; text-align: center; color: #000;
  }
</style>
</head>
<body>
<div class="canvas">
  <div class="book-wrap">
    <section class="back-cover">
      <div class="blurb">
        <p>Lorem ipsum dolor sit amet, consectetuer adipiscing elit, sed diam nonummy nibh euismod tincidunt ut laoreet dolore magna aliquam erat volutpat. Ut wisi enim ad minim veniam, quis nostrud exerci tation ullamcorper suscipit lobortis nisl ut aliquip ex ea commodo consequat. Duis autem vel eum iriure dolor in hendrerit in vulputate velit esse molestie consequat, vel illum dolore eu feugiat nulla facilisis at vero eros et accumsan et iusto odio dignissim qui blandit praesent luptatum zzril delenit augue duis dolore te feugait nulla facilisi.</p>
        <p>Lorem ipsum dolor sit amet, cons ectetuer adipiscing elit, sed diam nonummy nibh euismod tincidunt ut laoreet dolore magna aliquam erat volutpat. Ut wisi enim ad minim veniam, quis nostrud exerci tation ullamcorper suscipit lobortis nisl ut aliquip ex ea commodo consequat.</p>
        <p>Lorem ipsum dolor sit amet, consectetuer adipiscing elit, sed diam nonummy nibh euismod tincidunt ut laoreet dolore magna aliquam erat volutpat. Ut wisi enim ad minim veniam, quis nostrud exerci tation ullamcorper suscipit lobortis nisl ut aliquip ex ea commodo consequat. Duis autem vel eum iriure dolor in hendrerit in vulputate velit esse molestie</p>
      </div>
      <div class="author-band">
        <div class="author-photo" role="img" aria-label="Author portrait photo in front of a brick wall"></div>
        <p class="author-bio">Lorem ipsum dolor sit amet, consectetuer adipiscing elit, sed diam nonummy nibh euismod tincidunt ut laoreet dolore magna aliquam erat volutpat. Ut wisi enim ad minim veniam, quis nostrud exerci tation ullamcorper suscipit lobortis nisl ut aliquip ex ea commodo consequat. Duis</p>
      </div>
      <div class="barcode-box"></div>
    </section>

    <div class="spine-title">GOLDEN HANDSHAKE HOURS</div>

    <section class="front-cover">
      <div class="front-scene" role="img" aria-label="Blurred photo of a conference audience with microphones and a water jug on a white-clothed table"></div>
      <h1 class="book-title">
        <span class="title-red">Golden</span>
        <span class="title-gold">Handshake</span>
        <span class="title-red">Hours</span>
      </h1>
      <p class="book-subtitle">How We Turned Coffee Chats Into Fortunes With Friends Worth Keeping</p>
      <p class="author-name">AUTHOR NAME</p>
    </section>
  </div>
</div>
</body>
</html>
```